Landing Page - Mortgage Loan Intake

We are a mortgage company seeking a clean, easy-to-use landing page that consists of minimal copy and creative with a short intake form for customers to sign up to work with us on securing their home financing. We will soon have PX and Vormix campaigns running throughout the US, and those ads will lead to this landing page. We need at least one landing page for now and may need a slightly different version for A/B testing,. We will expand the project at the beginning of next year with additional versions with the same branding, just geared towards slightly different loan products.

This is the existing intake form we would incorporate on our landing page:

https://apply.brovanta.com/#/create-account

Here is some of the existing content that we would use as a springboard for the design, color scheme, and content of the landing page:

https://kelwinmortgage.com/https://kelwinmortgage.com/about/https://kelwinmortgage.com/refinance/consolidate-debt/

I have also included images that are related to what we're looking for either visually (feel and format) or in terms of the message.

Target Market(s)

people (borrowers) looking for a refinance or debt consolidation through a refinance

Industry/Entity Type

Mortgage Lender

Number of Pages Required

1 page

Font styles to use
Other font styles liked:
• unsure of the name but we would use the font currently used on kelwinmortgage.com

Colors
9bcb3b
cee9f5
ffffff
85acd3
cfeae6
abd036
cadf82
cedeed

Requirements
Must have
• intake form, clean light feel
Nice to have
• explanation of debt consolidation benefits or easy process via a simple infographic or illustration with a clean layout
Should not have
• anything off-brand (colors that are too heavy or not clean and airy)

```html
<!DOCTYPE html>
<html lang="en">
<head>
<meta charset="utf-8">
<title>Brovanta – Consolidate Debt</title>
<link href="https://fonts.googleapis.com/css2?family=Poppins:wght@300;400;600;700&display=swap" rel="stylesheet">
<style>
  :root {
    --canvas-bg: #ececec;
    --white: #ffffff;
    --brand-green: #9bcb3b;
    --button-green: #8cc63f;
    --band-blue: #0a7cc1;
    --band-blue-deep: #0873b4;
    --ink: #111111;
    --muted: #6d6d6d;
    --rule: #e3e3e3;
    --icon-blue: #85acd3;
    --icon-mint: #cfeae6;
    --icon-sky: #cee9f5;
  }
  * { box-sizing: border-box; margin: 0; padding: 0; }
  html, body {
    width: 1200px; height: 900px; overflow: hidden;
    background: var(--canvas-bg);
    font-family: "Poppins", sans-serif;
  }
  .page {
    position: absolute; left: 0; top: 75px;
    width: 1200px; height: 750px;
    background: var(--white);
    overflow: hidden;
  }
  .site-header {
    position: absolute; left: 0; top: 0; width: 100%; height: 91px;
    border-bottom: 1px solid var(--rule);
    background: var(--white);
  }
  .brand {
    position: absolute; left: 0; top: 16px; width: 100%;
    text-align: center;
  }
  .brand-name {
    display: block;
    font-weight: 600; font-size: 34px; line-height: 40px;
    color: var(--brand-green); letter-spacing: -0.5px;
  }
  .brand-tag {
    display: block;
    font-size: 8px; font-weight: 600; color: var(--muted); line-height: 12px;
  }
  .cta-button {
    position: absolute; left: 926px; top: 24px; width: 166px; height: 43px;
    border: 2px solid var(--button-green);
    color: var(--button-green);
    font-weight: 600; font-size: 19px;
    display: flex; align-items: center; justify-content: center;
    text-decoration: none;
  }
  .icon-strip {
    position: absolute; left: 422px; top: 91px; width: 352px; height: 14px;
    background: linear-gradient(90deg, var(--brand-green), var(--icon-blue) 30%, var(--icon-mint) 55%, var(--icon-sky) 75%, var(--brand-green) 90%, var(--icon-mint));
    opacity: 0.7;
    border-radius: 0 0 6px 6px;
  }
  .tax-band {
    position: absolute; left: 0; top: 226px; width: 100%; height: 322px;
    background: linear-gradient(180deg, var(--band-blue) 0%, var(--band-blue) 78%, var(--band-blue-deep) 78%, var(--band-blue-deep) 93%, var(--band-blue) 93%);
    color: var(--white); text-align: center;
  }
  .tax-band h2 {
    position: absolute; left: 0; top: 76px; width: 100%;
    font-weight: 700; font-size: 38px; line-height: 50px; letter-spacing: -0.3px;
  }
  .tax-band p {
    position: absolute; left: 117px; top: 146px; width: 966px;
    font-weight: 300; font-size: 14.6px; line-height: 21px;
  }
  .consolidate-heading {
    position: absolute; left: 113px; top: 676px;
    font-weight: 700; font-size: 29px; line-height: 43px; color: var(--ink);
    width: 300px;
  }
  .form-intro {
    position: absolute; left: 482px; top: 648px; width: 606px;
    text-align: center;
    font-weight: 300; font-size: 20px; letter-spacing: 1.4px; color: var(--muted);
  }
  .intake-card {
    position: absolute; left: 482px; top: 699px; width: 606px; height: 120px;
    background: var(--white);
    border-radius: 6px;
    box-shadow: 0 0 14px rgba(0,0,0,0.06);
  }
  .field {
    position: absolute; left: 30px; top: 29px; width: 265px; height: 38px;
    border: 1px solid #d8d8d8; border-radius: 3px;
    display: flex; align-items: flex-start; gap: 8px;
    padding: 12px 10px 0;
    font-size: 10px; color: #aaa;
  }
  .divider {
    position: absolute; left: 331px; top: 30px; width: 1px; height: 60px; background: var(--rule);
  }
  .secure-note {
    position: absolute; left: 355px; top: 31px; width: 220px;
  }
  .secure-note strong { display: block; font-size: 10px; font-weight: 600; color: #222; line-height: 14px; }
  .secure-note span { display: block; font-size: 8.5px; color: #888; line-height: 13px; }
</style>
</head>
<body>
  <main class="page">
    <header class="site-header">
      <div class="brand">
        <span class="brand-name">Brovanta</span>
        <span class="brand-tag">By Kelwin Mortgage</span>
      </div>
      <a class="cta-button" href="#apply">Get Started</a>
    </header>

    <div class="icon-strip" role="img" aria-label="Row of small home-finance illustration icons"></div>

    <section class="tax-band">
      <h2>Mortgage interest is tax-deductible.</h2>
      <p>The interest you pay on a credit card is not tax-deductible and you pay a higher rate than you would on your mortgage. Because of this, credit card debt is often referred to as “bad debt” whereas your mortgage is considered “good debt.” Using your home equity to pay off your high-interest credit card debt can save you money in the long run. Using your home equity, rather than your credit cards, to finance expensive purchases can also be a smart move. Be sure to consult your tax advisor. Trust us on this. Don't deduct and just cross your fingers for good luck. Know what you are doing before you mess with your taxes!</p>
    </section>

    <h3 class="consolidate-heading">When to consolidate your debt</h3>

    <p class="form-intro">Let's get started on your loan application</p>

    <form class="intake-card" id="apply">
      <label class="field">
        <svg width="12" height="9" viewBox="0 0 12 9" aria-hidden="true"><rect x="0.5" y="0.5" width="11" height="8" fill="none" stroke="#999"/><path d="M0.5 0.5 L6 5 L11.5 0.5" fill="none" stroke="#999"/></svg>
        Email Address
      </label>
      <div class="divider"></div>
      <div class="secure-note">
        <strong>Secure</strong>
        <span>Your data is protected with industry</span>
      </div>
    </form>
  </main>
</body>
</html>
```